Cobalt Press website re-design

We would like to recreate the www.cobaltpress-demo.com.au website into a simpler and more sophisticated version. We want the buyer to be drawn to our site and establish that we are reputable and professional from the moment they enter. We want them to easily find the product or service they are looking for within our site, decide that they would like to find out more and either click through to obtain a quote or click through to contact a rep.

The current website has been created using MS Front Page, however we would like the newly designed site to be created in a mobile responsive WordPress CMS format

We are a Print Broker who can save clients time in hunting around for the right supplier for their print jobs. This is most likely appealing to larger organisations who haven’t got time to waste in finding quotes from many different suppliers for each type of job. We make it easy because we have access to a large network of trade only print & signage suppliers so we can select the best and most cost effective supplier depending on the type of print job. Further, because we don’t do the printing in-house we have low overheads which means we can ensure competitive prices.
Updates

Target Market(s)

Business owners, print managers, receptionists, marketing managers who are time poor, uneducated re:printing, after quick & cost effective solutions

Industry/Entity Type

Printing

Requirements
Must have
• Use the current logo and colours - see files uploaded
Limit scrolling and keep pages within view
Easy to see buttons that navigate the buyer through the site
The site is to be clear, easy to understand, free from clutter (ie.ensure white space) and have a Professional/corporate look
Easy to use Quotation forms
Imagery needs to be modern, and clean -see brightmarrow site

Competitor/other websites we like and why?
I like brightmarrow.com.au for its’ modern look. I like how the products are displayed in High resolution are very clean and uncluttered. You can easily find the product and access ‘get a quote’.
Pelham Print has a good layout for the quote request. Check out pelhamprint-demo.com.au
www.vendrak.com.au are print brokers/managers. Their descriptions are easy to understand but still heavy in content.
Nice to have
• 1. Home Page
½ page summary of the core business
Distinct buttons for products and services down the side (so that people can go straight to what they need.)
About Us (including profiles); Products and Services; Get a Quote; Contact us across the top

2. About Us
A brief overview of owner, staff and reps. Click through to Profiles for each region rep and contact details either as pop ups or separate pages.

3. Products and Services
Buttons or lists of products link to pop up with get a quote link within (this could be grouped such as Business Cards, Letterheads, Folders etc.; Club printing with plastic cards, sign in books, coasters etc.; Marketing such as flyers, posters, banners etc. (Note. look at how others have broken it up)
Include calling for advice for special products and finishes as service on how a job can be improved and done within budget.
4. Get a Quote
(2 sites mentioned below that I like for the get a quote system)

5. Contact Us
Clear sections divided by lines and details large starting with 1300 number
Head office
Regional numbers and areas they cover
Include emails.

Contact us now or click to request a rep contact you.

```html
<!DOCTYPE html>
<html lang="en">
<head>
<meta charset="utf-8">
<title>Cobalt Press – Printing, Signage, Display</title>
<link href="https://fonts.googleapis.com/css2?family=Mulish:wght@400;600;700;800&family=Podkova:wght@400;600;700&display=swap" rel="stylesheet">
<style>
:root{
  --brand-red:#9a1220;
  --brand-red-dark:#6a0a12;
  --band-dark:#5c0810;
  --grey-band:#ebebeb;
  --text-grey:#4a4a4a;
  --logo-grey:#c9c9c9;
  --white:#ffffff;
  --cream:#f3dca0;
}
*{margin:0;padding:0;box-sizing:border-box}
html,body{width:1200px;height:1093px;overflow:hidden}
body{font-family:"Mulish",sans-serif;background:var(--white);color:var(--text-grey);position:relative}
.hero{position:absolute;left:0;top:0;width:1200px;height:403px;
  background:linear-gradient(180deg,#6f0f18 0%,#8a1420 60%,var(--brand-red) 100%)}
.band{position:absolute;left:0;width:1200px;height:11px;background:var(--band-dark)}
.header{position:absolute;left:171px;top:0;width:858px;height:74px;background:var(--white);
  border-radius:0 0 0 8px;box-shadow:0 2px 6px rgba(0,0,0,.35)}
.brand{position:absolute;left:10px;top:24px;display:flex;align-items:center;gap:8px;
  font-weight:800;font-size:20px;color:var(--brand-red)}
.brand-mark{width:22px;height:22px;background:var(--brand-red);border-radius:4px}
.nav{position:absolute;right:30px;top:30px;display:flex;gap:28px;font-size:15px;color:#222}
.nav .active{color:var(--brand-red)}
.hero-copy{position:absolute;left:172px;top:130px;width:475px;color:var(--white)}
.hero-title{font-family:"Podkova",serif;font-weight:700;font-size:31px;text-shadow:0 2px 3px rgba(0,0,0,.45);line-height:1}
.hero-sub{font-family:"Podkova",serif;font-size:21px;color:var(--cream);margin-top:6px}
.hero-text{font-size:13.6px;line-height:18px;margin-top:10px}
.hero-text strong{font-weight:700}
.quote-btn{display:inline-block;margin-top:22px;background:linear-gradient(#fff,#e2e2e2);color:var(--brand-red);
  font-weight:700;font-size:17px;padding:5px 10px;border-radius:4px;box-shadow:0 2px 3px rgba(0,0,0,.4)}
.call{font-weight:700;font-size:16.5px;margin-top:16px;padding-left:3px}
.hero-photo{position:absolute;left:686px;top:144px;width:324px;height:212px;border-radius:0 0 10px 0;
  background:linear-gradient(135deg,#a08a64,#d9c79f 50%,#c98a44);box-shadow:0 2px 6px rgba(0,0,0,.45)}
.values{position:absolute;left:0;top:414px;width:1200px;height:141px;background:var(--grey-band);text-align:center}
.values-top{font-weight:800;font-size:20px;color:#444;margin-top:32px;letter-spacing:.2px}
.values-main{font-weight:800;font-size:29px;color:var(--brand-red);line-height:30px}
.intro{position:absolute;left:260px;top:588px;width:680px;text-align:center;font-size:14.5px;line-height:21.5px}
.intro p+p{margin-top:20px}
.cta-line{position:absolute;left:483px;top:766px;width:253px;height:1px;background:#ccc}
.cta{position:absolute;left:522px;top:745px;padding:3px;border:1px solid #ccc;border-radius:5px;background:var(--white)}
.cta span{display:block;background:var(--brand-red);color:var(--white);font-size:15px;padding:8px 11px;border-radius:3px}
.clients{position:absolute;left:250px;top:852px;width:708px;height:40px;display:flex;align-items:center;justify-content:space-between}
.client{background:var(--logo-grey);border-radius:4px}
.footer{position:absolute;left:0;top:959px;width:1200px;height:134px;background:var(--brand-red);text-align:center;color:var(--white)}
.footer-nav{display:flex;justify-content:center;gap:24px;font-size:14px;margin-top:41px}
.footer-nav .active{color:#111}
.copyright{font-size:9.5px;margin-top:14px}
</style>
</head>
<body>
<section class="hero"></section>
<div class="band" style="top:403px"></div>

<header class="header">
  <div class="brand"><span class="brand-mark"></span>Cobalt Press</div>
  <nav class="nav">
    <span class="active">Home</span><span>About Us</span><span>Products and Services</span><span>Get a Quote</span><span>Contact Us</span>
  </nav>
</header>

<div class="hero-copy">
  <h1 class="hero-title">Printing • Signage • Display</h1>
  <p class="hero-sub">Your Commercial Printing &amp; Signage Specialist</p>
  <p class="hero-text">Lumen Varnish is an exclusive NEW UV finish achieving a matt &amp; gloss UV on the one surface in one pass at perfect registration - ideal for business cards, flyers, booklet covers, presentation folders &amp; packaging <strong>- ask for a sample today!</strong></p>
  <span class="quote-btn">Ask for a free Quote</span>
  <p class="call">Call 1300 555 018 to discuss your job or ask us for a quote.</p>
</div>
<div class="hero-photo" role="img" aria-label="Close-up photo of a printed business card with raised red UV lettering"></div>

<section class="values">
  <p class="values-top">LOW COST &nbsp;-&nbsp; LATEST TECHNOLOGY &nbsp;-&nbsp; FAST TURNAROUND PREMIUM QUALITY</p>
  <p class="values-main">FROM AUSTRALIA'S LEADING SPECIALIST<br>TRADE SUPPLIERS</p>
</section>

<section class="intro">
  <p>Using Australia's leading print trade suppliers, we provide our clients with the most cost effective print solution in the market. We are constantly sourcing the most advanced technology in the industry to produce the lowest unit price, best quality and fastest Australia wide delivery.</p>
  <p>From small run digital, to offset, wide-format, signage, packaging, point of sale or specialist hotel, retail &amp; club supplies our product knowledge is second to none.</p>
</section>

<div class="cta-line"></div>
<div class="cta"><span>Products and Services</span></div>

<div class="clients" aria-label="Client list">
  <svg width="14" height="20" viewBox="0 0 14 20"><path d="M11 2 3 10l8 8" fill="none" stroke="#444" stroke-width="4"/></svg>
  <div class="client" style="width:48px;height:32px"></div>
  <div class="client" style="width:44px;height:26px"></div>
  <div class="client" style="width:44px;height:26px;border-radius:50%"></div>
  <div class="client" style="width:48px;height:18px"></div>
  <div class="client" style="width:38px;height:36px"></div>
  <div class="client" style="width:32px;height:32px;border-radius:50%"></div>
  <div class="client" style="width:62px;height:18px"></div>
  <div class="client" style="width:52px;height:20px"></div>
  <svg width="14" height="20" viewBox="0 0 14 20"><path d="M3 2l8 8-8 8" fill="none" stroke="#444" stroke-width="4"/></svg>
</div>

<div class="band" style="top:948px"></div>
<footer class="footer">
  <nav class="footer-nav">
    <span class="active">Home</span><span>About Us</span><span>Products and Services</span><span>Get a Quote</span><span>Contact Us</span>
  </nav>
  <p class="copyright">Copyright Cobalt Press - A Division of Harbourline Trade Group Pty Limited</p>
</footer>
</body>
</html>
```